Criação de Kit com 5 Layouts de Post para Redes Sociais (Facebook, Instagram e etc) para Construção & Engenharia
A empresa queria:
" Trabalho com a elaboração de projetos de engenharia em geral, sendo o maior foco e experiência os proj. de Prevenção e combate a incêndio, mas tbm na elaboração de projetos arquitetônico, estrutural, e de interiores. Regularização de obras junto a Prefeitura, Corpo de Bombeiros, Junta Ouromar, Vigilância Sanitária. Acompanhamento de Obras. "

```html
<!DOCTYPE html>
<html lang="pt-BR">
<head>
<meta charset="UTF-8">
<title>Helena Castro — Projetos</title>
<link rel="stylesheet" href="https://fonts.googleapis.com/css2?family=Montserrat:wght@400;500;700;800&display=swap">
<style>
:root{
  --green:#27382f;
  --green-deep:#1f2e26;
  --gold-1:#b98f4c;
  --gold-2:#e9d19a;
  --gold-3:#c9a45f;
  --cream:#f1e6c8;
  --ink:#27382f;
}
*{margin:0;padding:0;box-sizing:border-box}
html,body{width:1200px;height:1200px;overflow:hidden;background:#fff}
.canvas{position:relative;width:1200px;height:1200px;overflow:hidden;font-family:'Montserrat',sans-serif;background:var(--green)}
.photo{position:absolute;left:640px;top:0;width:560px;height:1200px;
  background:linear-gradient(160deg,#f4f3f0 0%,#e6e4df 35%,#cfd0d2 60%,#8d8f96 85%,#5a5d68 100%)}
.gold{background:linear-gradient(90deg,var(--gold-1),var(--gold-2) 55%,var(--gold-3))}
.headline{position:absolute;left:62px;top:70px;width:560px;color:var(--cream);
  font-weight:800;font-size:45px;line-height:57px;letter-spacing:1px}
.band{position:absolute;left:0;top:222px;width:640px;height:136px}
.band-text{position:absolute;left:62px;top:254px;color:var(--ink);font-weight:700;font-size:32px;line-height:40px;letter-spacing:.5px}
.services{position:absolute;left:58px;top:404px;list-style:none}
.services li{display:flex;align-items:flex-start;color:#e9e3d3;font-size:33px;font-weight:500;line-height:40px;margin-bottom:58px}
.services li.two{margin-bottom:46px}
.services li:nth-child(3),.services li:nth-child(4){margin-bottom:62px}
.services svg{flex:0 0 auto;width:56px;height:50px;margin-right:50px}
.divider{position:absolute;left:58px;top:918px;width:534px;height:2px}
.brand{position:absolute;left:0;top:985px;width:640px;text-align:center}
.brand-mark{display:block;margin:0 auto 22px;width:56px;height:56px;border:3px solid var(--gold-3)}
.brand-name{color:#ecebe6;font-size:40px;font-weight:500;letter-spacing:4px}
.brand-tag{margin-top:6px;color:var(--gold-3);font-size:13px;letter-spacing:2.6px;font-weight:500}
.top-bar{position:absolute;left:732px;top:140px;width:326px;height:34px}
.diamond{position:absolute;transform:rotate(45deg)}
.d1{left:611px;top:610px;width:56px;height:56px}
.d2{left:627px;top:722px;width:26px;height:26px}
.d3{left:1098px;top:1040px;width:34px;height:34px}
.d4{left:1150px;top:1034px;width:40px;height:40px}
.contact{position:absolute;left:792px;top:1076px;width:408px;height:124px;padding:22px 0 0 30px;color:var(--ink)}
.contact h3{font-size:20px;font-weight:500;letter-spacing:1.5px;margin-bottom:8px}
.contact p{display:flex;align-items:center;font-size:23px;font-weight:500;line-height:38px}
.contact p.mail{font-size:21px}
.contact svg{width:26px;height:26px;margin-right:12px}
</style>
</head>
<body>
<div class="canvas">
  <div class="photo" role="img" aria-label="Fotografia de mesa de trabalho com plantas arquitetônicas, notebook, tablet e mãos desenhando com lápis"></div>

  <h1 class="headline">ESTÁ PRECISANDO<br>DE UM PROJETO?</h1>

  <div class="band gold"></div>
  <h2 class="band-text">REALIZAMOS PROJETOS<br>DE QUALIDADE PARA</h2>

  <ul class="services">
    <li class="two"><svg viewBox="0 0 56 50"><rect x="3" y="10" width="38" height="36" fill="none" stroke="#c9a45f" stroke-width="4"/><path d="M12 26l10 11L52 6" fill="none" stroke="#e9d19a" stroke-width="6"/></svg><span>PREVENÇÃO E COMBATE<br>A INCÊNDIO</span></li>
    <li><svg viewBox="0 0 56 50"><rect x="3" y="10" width="38" height="36" fill="none" stroke="#c9a45f" stroke-width="4"/><path d="M12 26l10 11L52 6" fill="none" stroke="#e9d19a" stroke-width="6"/></svg><span>ARQUITETÔNICO</span></li>
    <li><svg viewBox="0 0 56 50"><rect x="3" y="10" width="38" height="36" fill="none" stroke="#c9a45f" stroke-width="4"/><path d="M12 26l10 11L52 6" fill="none" stroke="#e9d19a" stroke-width="6"/></svg><span>ESTRUTURAL</span></li>
    <li><svg viewBox="0 0 56 50"><rect x="3" y="10" width="38" height="36" fill="none" stroke="#c9a45f" stroke-width="4"/><path d="M12 26l10 11L52 6" fill="none" stroke="#e9d19a" stroke-width="6"/></svg><span>HIDROSSANITÁRIO</span></li>
    <li><svg viewBox="0 0 56 50"><rect x="3" y="10" width="38" height="36" fill="none" stroke="#c9a45f" stroke-width="4"/><path d="M12 26l10 11L52 6" fill="none" stroke="#e9d19a" stroke-width="6"/></svg><span>INTERIORES</span></li>
  </ul>

  <div class="divider gold"></div>

  <div class="brand">
    <span class="brand-mark"></span>
    <div class="brand-name">HELENA CASTRO</div>
    <div class="brand-tag">PROJETANDO COM QUALIDADE E SEGURANÇA</div>
  </div>

  <div class="top-bar gold"></div>
  <div class="diamond d1 gold"></div>
  <div class="diamond d2 gold"></div>

  <div class="contact gold">
    <h3>ENTRE EM CONTATO</h3>
    <p><svg viewBox="0 0 26 26"><circle cx="13" cy="13" r="11" fill="none" stroke="#27382f" stroke-width="2.5"/></svg>(31) 98765 4321</p>
    <p class="mail"><svg viewBox="0 0 26 26"><rect x="2" y="5" width="22" height="16" rx="2" fill="#27382f"/><path d="M3 7l10 8 10-8" fill="none" stroke="#e9d19a" stroke-width="2"/></svg>helenacastro@exemplo.com</p>
  </div>
  <div class="diamond d3 gold"></div>
  <div class="diamond d4 gold"></div>
</div>
</body>
</html>
```